Business Card for a Candle Company. - Creative Hipster Styling :)

I am after a two sided Business Card. Contact information on the front, text that will be supplied (and details further on here) on the back. Ideally I am looking for someone I can continue to work with in the future for flyers, labels, marketing material etc.

I have a Logo which I am using as the labels for the candle and have attached all the versions of the file I was given. I am after a similar feel to my logo and love the font and the feather used. it is important that my card looks like it is meant to go with the logo.

I would love you to use your imagination and see what can be thought up :)

All my candles are either clear or black glass and packaging is black and labels are white, on a square label with black writing (see attachments)

I love the feather on the logo if it can be incorporated great, if the business card looks better without it than that is fine too..

Target Market(s)

I am a new candle company and the feel I'm going for is a little luxury a little hipster. Imagine the candle going into a converted warehouse studio in the city.

Industry/Entity Type

Home And Garden

Contact Information for Business Card

I have a Logo which I am using as the labels for the candle and have attached all the versions of the file I was given. I am after a similar feel to my logo and love the font used but its caps and I don't really want everything in CAPS. It is important thought that everything goes together.

I love the feather on the logo if it can be incorporated great, if the business card looks better without it than that is fine too.

Norrel Glow Co
Central Coast, NSW Australia
A little wax company, in a garage, on the coast.
craftmarketa.com/au/shop/NorrelGlowCo
sociallinka.com.au/norrelglowco
norrelglowco@mailbrook.com.au
Jess Pendell
0481 276 152.

On the back of the card I need it to look good and go with the design on the front but want a bit of text;

To give you an idea of what I want on the back I've put what I've got following but I'm still working on grammar and wording so it may change slightly before the final edit.

We would love to see how you display your candle or reuse the glass vessel and would love to see a photo!
Check out ideas and share yours on your social media #norrelglowco

Just a few ideas to reuse your vessel;

A Vase to Display fresh flowers
Lolly Jar for your favourite candy
Decorate with baubles at Christmas
Bathroom Vanity Storage
Decorate with eggs at Easter
Plant a teranium inside.

Font styles to use
Decorative
Script
Other font styles liked:
• OctinVintageFree

Colors
000000
ffffff
757575

Requirements
Must have
• The only must is that it needs to look like it goes with my logo which I am using as the labels on the actual candle. the labels are white with black details and are square.
• Not too structured if possible as it is a creative company rather that a professional services company.
• I want people to pick up the card and think it looks great. I believe a business card is a very useful marketing tool and should be used as such. One card will be included in with each candle so that customers can re order.
Nice to have
• I love the feather on the logo if it can be incorporated great, if the business card looks better without it than that is fine too.
• Card just needs to fit with the logo.
Should not have
• It should not be a boring card. :)

```html
<!DOCTYPE html>
<html lang="en">
<head>
<meta charset="utf-8">
<title>Norrel Glow Co — Business Card</title>
<link href="https://fonts.googleapis.com/css2?family=Ubuntu:wght@400;500&display=swap" rel="stylesheet">
<style>
  :root {
    --page: #e9e6e2;
    --card-black: #0e0e0e;
    --card-black-soft: #1a1a1a;
    --wax-brown: #3e2a1f;
    --bullet-brown: #6e4c34;
    --swoosh-white: #f2f2f2;
    --swoosh-grey: #757575;
    --text-white: #ffffff;
    --logo-grey: #d9d9d9;
    --feather-dark: #262626;
    --feather-mid: #333333;
  }
  * { margin: 0; padding: 0; box-sizing: border-box; }
  html, body {
    width: 1200px; height: 900px; overflow: hidden;
    background: var(--page);
    font-family: "Ubuntu", "Open Sans", sans-serif;
  }
  .canvas { position: relative; width: 1200px; height: 900px; }

  .card {
    position: absolute;
    width: 620px; height: 354px;
    background: radial-gradient(ellipse at 60% 30%, var(--card-black-soft), var(--card-black) 70%);
    overflow: hidden;
    box-shadow: 0 10px 28px rgba(0,0,0,0.28);
  }
  .card--back { left: 120px; top: 70px; }
  .card--front { left: 460px; top: 470px; }

  /* Back side */
  .reuse-list {
    position: absolute; left: 44px; top: 92px;
    list-style: none; z-index: 2;
  }
  .reuse-list li {
    position: relative;
    color: var(--text-white);
    font-size: 16px; line-height: 29px;
    padding-left: 26px;
  }
  .reuse-list li::before {
    content: ""; position: absolute; left: 0; top: 10px;
    width: 10px; height: 10px; border-radius: 50%;
    background: var(--bullet-brown);
  }
  .feather-art {
    position: absolute; left: 230px; top: 20px;
    width: 380px; height: 320px; z-index: 1;
  }

  /* Front side */
  .wave { position: absolute; left: 0; top: 0; width: 620px; height: 354px; }
  .brand {
    position: absolute; right: 48px; top: 70px;
    display: flex; align-items: center; gap: 10px;
  }
  .brand__mark {
    width: 12px; height: 12px; border-radius: 50%;
    background: var(--bullet-brown);
  }
  .brand__name {
    color: var(--logo-grey);
    font-size: 24px; font-weight: 400;
    letter-spacing: 3px; text-transform: uppercase;
  }
  .contact {
    position: absolute; left: 38px; top: 180px;
    list-style: none;
  }
  .contact li {
    display: flex; align-items: center; gap: 10px;
    color: var(--text-white);
    font-size: 16px; line-height: 26px;
  }
  .contact svg { width: 14px; height: 14px; flex: none; }
</style>
</head>
<body>
<main class="canvas">

  <section class="card card--back" aria-label="Card back">
    <ul class="reuse-list">
      <li>A Vase to Display fresh flowers</li>
      <li>Lolly Jar for your favourite candy</li>
      <li>Decorate with baubles at Christmas</li>
      <li>Bathroom Vanity Storage</li>
      <li>Decorate with eggs at Easter</li>
      <li>Plant a teranium inside.</li>
    </ul>
    <svg class="feather-art" viewBox="0 0 380 320" role="img" aria-label="Large faint feather illustration">
      <defs>
        <linearGradient id="featherTone" x1="0" y1="1" x2="1" y2="0">
          <stop offset="0" stop-color="var(--feather-dark)"/>
          <stop offset="1" stop-color="var(--feather-mid)"/>
        </linearGradient>
      </defs>
      <ellipse cx="200" cy="150" rx="190" ry="52" transform="rotate(-38 200 150)" fill="url(#featherTone)" opacity="0.85"/>
    </svg>
  </section>

  <section class="card card--front" aria-label="Card front">
    <svg class="wave" viewBox="0 0 620 354" aria-hidden="true">
      <path d="M0,276 C170,318 340,282 455,205 C370,282 190,322 0,306 Z" fill="var(--swoosh-grey)"/>
      <path d="M0,284 C170,322 345,286 460,206 C380,284 190,326 0,314 Z" fill="var(--swoosh-white)"/>
      <path d="M0,312 C190,330 360,292 450,226 C510,184 565,172 620,168 L620,354 L0,354 Z" fill="var(--wax-brown)"/>
    </svg>

    <div class="brand">
      <span class="brand__mark"></span>
      <span class="brand__name">Norrel Glow Co</span>
    </div>

    <ul class="contact">
      <li>
        <svg viewBox="0 0 14 14" aria-hidden="true"><path d="M3 1 L5 1 L6 4 L4.5 5.3 C5.3 7 6.9 8.6 8.7 9.5 L10 8 L13 9 L13 11 C13 12 12 13 11 13 C5.5 12.6 1.4 8.5 1 3 C1 2 2 1 3 1 Z" fill="var(--bullet-brown)"/></svg>
        0481 276 152
      </li>
      <li>
        <svg viewBox="0 0 14 14" aria-hidden="true"><rect x="1" y="3" width="12" height="8" fill="var(--bullet-brown)"/><path d="M1 3 L7 8 L13 3" stroke="var(--card-black)" stroke-width="1" fill="none"/></svg>
        norrelglowco@mailbrook.com.au
      </li>
      <li>
        <svg viewBox="0 0 14 14" aria-hidden="true"><rect x="1" y="1" width="12" height="12" fill="var(--bullet-brown)"/></svg>
        craftmarketa.com/au/shop/NorrelGlowCo
      </li>
      <li>
        <svg viewBox="0 0 14 14" aria-hidden="true"><rect x="1" y="1" width="12" height="12" fill="var(--bullet-brown)"/></svg>
        sociallinka.com.au/norrelglowco
      </li>
    </ul>
  </section>

</main>
</body>
</html>
```